political advertisement for magazine

9.135 in 12.125 in. My wife is running for Judge. She needs an ad for an African-American Magazine ASAP . The ad is about a testimonial by one of her clients that makes her relatable to the African-American community. I am uploading the text for the testimonial, the picture of my wife and her client, her logo, a possible backdrop and also a slogan.

This is going in a church publication geared toward the African American Community

• The image of all the people in the back. On top of that image, you have "The people stand behind Lorena for Circuit Court Judge". Also you have a letter from her client with a picture of both of them. Also include the vote for Lorena logo and her headshot. The above is just my idea if you have an idea that is totally different but portrays that Lorena is for the people, I am ok with that too. thanks!

```html
<!DOCTYPE html>
<html lang="en">
<head>
<meta charset="utf-8">
<title>Lorena for Circuit Court Judge – Magazine Ad</title>
<link rel="stylesheet" href="https://fonts.googleapis.com/css2?family=Playfair+Display:wght@700&family=Open+Sans:ital,wght@0,400;1,400;1,600&family=Oswald:wght@300&display=swap">
<style>
  :root {
    --navy: #1f3f8c;
    --red: #d0202e;
    --ink: #2f3444;
    --paper: #ffffff;
    --stage: #e9eaee;
    --crowd-light: #e4e6ec;
    --crowd-mid: #b9bec9;
    --crowd-dark: #9aa0ad;
    --photo-a: #c9c3bd;
    --photo-b: #3b3a40;
  }
  * { box-sizing: border-box; margin: 0; padding: 0; }
  html, body { width: 778px; height: 1200px; overflow: hidden; }
  body { background: var(--stage); position: relative; font-family: "Open Sans", sans-serif; }

  .ad {
    position: absolute; left: 19px; top: 109px;
    width: 740px; height: 982px;
    background: var(--paper);
    border: 9px solid var(--navy);
    box-shadow: 0 6px 24px rgba(0,0,0,.18);
    overflow: hidden;
  }

  .crowd {
    position: absolute; left: 0; right: 0; top: 240px; height: 500px;
    background:
      linear-gradient(180deg, var(--paper) 0%, rgba(255,255,255,0) 22%, rgba(255,255,255,0) 78%, rgba(255,255,255,.6) 100%),
      linear-gradient(90deg, var(--crowd-mid) 0%, var(--crowd-light) 25%, var(--crowd-dark) 50%, var(--crowd-light) 75%, var(--crowd-mid) 100%);
  }
  .crowd-veil {
    position: absolute; left: 30px; right: 30px; top: 300px; height: 380px;
    background: rgba(255,255,255,.78);
  }

  .campaign-name {
    position: absolute; left: 40px; top: 44px; width: 360px;
    display: flex; align-items: flex-start; gap: 14px;
    font-family: "Playfair Display", serif; font-weight: 700;
    color: var(--red); font-size: 38px; line-height: 1.2; letter-spacing: 1px;
  }
  .campaign-name .dot {
    flex: none; width: 14px; height: 14px; margin-top: 16px;
    background: var(--red); border-radius: 50%;
  }

  .headshot {
    position: absolute; right: 36px; top: 26px;
    width: 236px; height: 236px; border-radius: 50%;
    border: 7px solid var(--navy);
    background: radial-gradient(circle at 50% 40%, var(--photo-a) 0 38%, var(--photo-b) 72%);
  }

  .testimonial {
    position: absolute; left: 46px; right: 46px; top: 318px;
    color: var(--ink); font-style: italic; font-size: 15.5px; line-height: 1.55;
  }
  .testimonial p { margin-bottom: 14px; }
  .testimonial .signer { color: var(--red); font-weight: 600; }

  .rally-band {
    position: absolute; left: 0; right: 0; bottom: 0; height: 250px;
    background: var(--navy);
    border-top: 6px solid var(--red);
    text-align: center; color: var(--paper);
  }
  .rally-band .frame {
    position: absolute; left: 16px; right: 16px; top: 14px; bottom: 44px;
    border: 2px solid rgba(255,255,255,.75);
    padding-top: 14px;
  }
  .rally-band .lead {
    font-family: "Oswald", sans-serif; font-weight: 300;
    font-size: 30px; line-height: 36px; letter-spacing: 3px;
  }
  .rally-band .name {
    font-family: "Playfair Display", serif; font-weight: 700;
    color: var(--red); font-size: 80px; line-height: 82px; letter-spacing: 3px;
  }
  .rally-band .seat {
    font-family: "Oswald", sans-serif; font-weight: 300;
    font-size: 28px; line-height: 34px; letter-spacing: 3px;
  }
  .rally-band .disclaimer {
    position: absolute; left: 0; right: 0; bottom: 14px;
    font-size: 9.5px; line-height: 14px; color: rgba(255,255,255,.85);
  }
</style>
</head>
<body>
  <section class="ad" aria-label="Lorena for Circuit Court Judge advertisement">
    <div class="crowd" role="img" aria-label="Faded photo of a crowd of supporters"></div>
    <div class="crowd-veil"></div>

    <div class="campaign-name">
      <span class="dot"></span>
      <span>Vote Lorena Whitfield for Judge</span>
    </div>

    <div class="headshot" role="img" aria-label="Portrait photo of the candidate"></div>

    <article class="testimonial">
      <p>For the past two years, Lorena Whitfield has been my lawyer. She has always strived to provide excellence in legal services. Her almost encyclopedic knowledge of the law makes for a flawless, precise, navigation of the legal system, with results.</p>
      <p>She is the epitome of professionalism, that is aptly balanced by her calm persona. Her empathy is more than commendable, and her legal experience unmatched.</p>
      <p>Lorena Whitfield is truly one of kind, deserving of all accolades, appointments, and accomplishments.</p>
      <p>Yours Truly,<br><span class="signer">Denise Carter</span></p>
    </article>

    <footer class="rally-band">
      <div class="frame">
        <p class="lead">THE PEOPLE STAND BEHIND</p>
        <p class="name">LORENA</p>
        <p class="seat">FOR CIRCUIT COURT JUDGE</p>
      </div>
      <p class="disclaimer">Political advertisement paid for and approved by the Committee to Elect Lorena Whitfield for Circuit Court Judge.</p>
    </footer>
  </section>
</body>
</html>
```